Velmora EIRL Business Card Design Project

We need a business card design for a New Business Intelligence Consultant. We bring a complete service to the client from first consulting meeting to help desk and system improvement.

I will upload the company logo and I like to use the logo colors on the card. Feel free to use all logo components on the design, for example one side with the black logo using complete card and the other side only the red shape (is an example, feel absolutely free :)).

The principal idea is to sell a professional service and a modern company.

Target Market(s)

IT Business Intelligence Clients

Industry/Entity Type

Professional Service

Requirements
Nice to have
• - Use the logo colors and minimize white sections.
- Rounded borders
Should not have
• I don't want to see any references to people working on a meeting or office photos or any computers related logos.

```html
<!DOCTYPE html>
<html lang="en">
<head>
<meta charset="utf-8">
<title>Velmora EIRL — Business Card</title>
<link href="https://fonts.googleapis.com/css2?family=Source+Sans+3:wght@400;600;700&display=swap" rel="stylesheet">
<style>
  :root {
    --backdrop: #b0872c;
    --card-black: #000000;
    --card-grey: #a7a8ab;
    --brand-red: #ed1c24;
    --brand-grey: #a4a5a8;
    --rule-grey: #9b9ca0;
    --ink-dark: #141414;
    --text-white: #ffffff;
    --font-main: "Source Sans 3", "Myriad Pro", Arial, sans-serif;
  }
  * { box-sizing: border-box; margin: 0; padding: 0; }
  html, body {
    width: 1200px; height: 686px; overflow: hidden;
    background: var(--backdrop);
    font-family: var(--font-main);
  }
  .stage { position: relative; width: 1200px; height: 686px; }

  .card {
    position: absolute;
    width: 526px; height: 301px;
    border-radius: 22px;
    overflow: hidden;
  }
  .card--front { left: 54px; top: 155px; background: var(--card-black); }
  .card--back  { left: 616px; top: 234px; background: var(--card-grey); }

  .rule { position: absolute; height: 3px; background: var(--rule-grey); top: 124px; }
  .rule--lead  { left: 0; width: 34px; }
  .rule--main  { left: 270px; width: 193px; }
  .rule--tail  { left: 494px; width: 31px; }

  .brand {
    position: absolute; left: 40px; top: 103px;
    display: flex; align-items: center; gap: 12px;
  }
  .brand__square { width: 36px; height: 36px; background: var(--brand-grey); }
  .brand__name {
    font-size: 40px; font-weight: 600; line-height: 1;
    color: var(--brand-red); letter-spacing: -0.5px;
  }

  .identity, .address, .contacts {
    position: absolute; right: 63px; text-align: right;
  }
  .identity { top: 65px; }
  .identity__name { font-size: 17px; font-weight: 700; color: var(--brand-red); line-height: 20px; }
  .identity__title { font-size: 12.5px; font-weight: 700; color: var(--brand-grey); line-height: 18px; }

  .address { top: 139px; font-size: 13px; color: var(--text-white); line-height: 20px; }

  .contacts { right: 63px; top: 191px; list-style: none; }
  .contacts li {
    display: flex; justify-content: flex-end; align-items: center; gap: 5px;
    font-size: 12.5px; color: var(--text-white); line-height: 17px; height: 18px;
  }
  .contacts li:first-child { margin-bottom: 3px; }
  .contacts svg { width: 12px; height: 12px; flex: none; }
  .contacts .icon-slot { position: absolute; right: -16px; }
  .contacts li { position: relative; }

  .back-brand {
    position: absolute; inset: 0;
    display: flex; align-items: center; justify-content: center; gap: 16px;
  }
  .back-brand__square { width: 46px; height: 46px; background: var(--brand-red); }
  .back-brand__name {
    font-size: 58px; font-weight: 600; line-height: 1;
    color: var(--ink-dark); letter-spacing: -1px;
  }
</style>
</head>
<body>
<main class="stage">
  <section class="card card--front" aria-label="Card front">
    <div class="rule rule--lead"></div>
    <div class="brand">
      <span class="brand__square"></span>
      <span class="brand__name">velmora</span>
    </div>
    <div class="rule rule--main"></div>
    <div class="rule rule--tail"></div>

    <div class="identity">
      <p class="identity__name">Your Name</p>
      <p class="identity__title">Title</p>
    </div>

    <div class="address">
      <p>Complex name,Street name</p>
      <p>City, State, zip code</p>
    </div>

    <ul class="contacts">
      <li>123-456-7890
        <svg class="icon-slot" viewBox="0 0 12 12" aria-hidden="true"><path d="M2.2 1.2l2 1.8-.9 1.5c.7 1.6 1.8 2.8 3.4 3.6l1.4-.9 1.9 2-1.2 1.4C5.4 10.3 1.8 6.7 1 2.4z" fill="var(--brand-red)"/></svg>
      </li>
      <li>123-456-7890
        <svg class="icon-slot" viewBox="0 0 12 12" aria-hidden="true"><rect x="3" y="1" width="6" height="4" fill="none" stroke="var(--brand-red)" stroke-width="1.2"/><rect x="1" y="5" width="10" height="6" rx="1" fill="none" stroke="var(--brand-red)" stroke-width="1.2"/><line x1="3" y1="8" x2="9" y2="8" stroke="var(--brand-red)" stroke-width="1"/></svg>
      </li>
      <li>name@website.com
        <svg class="icon-slot" viewBox="0 0 12 12" aria-hidden="true"><circle cx="6" cy="6" r="2" fill="none" stroke="var(--brand-red)" stroke-width="1.4"/><path d="M8 4v3c0 1 1.5 1.4 2 0 .6-1.8.2-5-4-5.2A4.4 4.4 0 0 0 6 10.5c1 0 1.8-.2 2.4-.6" fill="none" stroke="var(--brand-red)" stroke-width="1.4"/></svg>
      </li>
      <li>www.website.com
        <svg class="icon-slot" viewBox="0 0 12 12" aria-hidden="true"><circle cx="6" cy="6" r="5" fill="none" stroke="var(--brand-red)" stroke-width="1.2"/><ellipse cx="6" cy="6" rx="2.2" ry="5" fill="none" stroke="var(--brand-red)" stroke-width="1"/><line x1="1" y1="6" x2="11" y2="6" stroke="var(--brand-red)" stroke-width="1"/></svg>
      </li>
    </ul>
  </section>

  <section class="card card--back" aria-label="Card back">
    <div class="back-brand">
      <span class="back-brand__square"></span>
      <span class="back-brand__name">velmora</span>
    </div>
  </section>
</main>
</body>
</html>
```